TROMP Diagnostics App - iOS

I need some UI artwork (2D) for my already released iOS app: "TROMP Kv" I'd like the UI to look more like an in-dash head-unit in a car. I'm in the process of updating the app with iPad support and would like to release this next version with a brand new UI.

A lot of car audio enthusiast already use my app and probably mount their iPhone/iPod near their car audio components on the dash. Most of the car audio deck Mfgs support a few colors: Green/Blue/Amber/Red I'd like to offer these themes as well. But I will settle for the Amber color to match my existing App icon scheme. (nice to have)

My UI is incredibly simple. It's just a bunch of up/down buttons. I plan to do some animations an will need some room blocked off for this to the left of LCD text.

Screenshots are of my existing iOS app for iPhone and the half assed job I did for iPad. - Note: These are the only two orientations I plan to use. But the resolution in these photos are smaller than my requirements. See "Must Haves" for all four resolutions.

update: I'd like something to imitate the style of the skin in the following: http://quorvak.pelmintra.example/art/Lumatone-XJR8-Skin-71845206

Thanks!

Target Market(s)

Car Audio Enthusiasts

Industry/Entity Type

Audio

Requirements
Must have
• - Static background that looks like an in-dash stereo. (think lumatone skin)
- An LCD area where I can display some text and stats on left (see iPad ss)
- UI buttons that support up/down states. When the user presses a button, it stays "down" until it's tapped again or another is pushed.
- UI toggle switch for Wobble mode (see ss)

iPhone/iPod resolutions
-
- Landscape for iPhone4/4S Retina (960 x 640)
- Landscape for iPhone 5 Retina (1136 x 640)

iPad resolutions
-
- This UI has more buttons and taller, but I'd like a similar look and feel
- Landscape for iPad Retina (2048 x 1536)
- Landscape for iPad2/mini (1024 x 768)

Other Controls:
- An empty space for UI slider control. I will place this over artwork. (see ss)
- Emergency stop button should be red and easily accessible. Slightly larger than other buttons.

iPhone Buttons/Controls
-
20,30,40,50,60,70,80,90,100,150,250,300
Toggle Switch, P button, S button, Stop button

iPad Buttons/Controls
-
20,25,30,35,40,45,50,55,60,65,70,80,90,110,125,150,250,300
Instant TROMP Buttons: 20,25,30,35,40,45,50,55

Disregard the waveform animation in the screenshots (squiggly line at bottom) I plan do a small animation to the left of the text in the LCD area.
Nice to have
• - Theme for LED-like colors: Green/Blue/Amber/Red on-off buttons
Should not have
• - sharp corners on buttons
- stretched version of iPhone layout for the iPad.

```html
<!DOCTYPE html>
<html lang="en">
<head>
<meta charset="utf-8">
<title>TROMP Kv – Head Unit UI</title>
<link rel="stylesheet" href="https://fonts.googleapis.com/css2?family=Orbitron:wght@400;500&family=Noto+Sans:wght@700&family=Oswald:wght@500&display=swap">
<style>
  :root {
    --page-bg: #5a1214;
    --screen-bg: #7c1a1d;
    --screen-grid: rgba(0,0,0,0.09);
    --lcd-top: #b58a8c;
    --lcd-bottom: #8e5a5d;
    --lcd-edge: #5c2426;
    --digit: #ffffff;
    --label: #f1e4e4;
    --panel: rgba(255,255,255,0.10);
    --key-top: #c7a8aa;
    --key-bottom: #9a7275;
    --key-down-top: #9b7477;
    --key-down-bottom: #b89597;
    --key-down-text: #5e1216;
    --switch-face: #f3f1f1;
    --switch-off: #b3141c;
    --stop-light: #f0262a;
    --stop-dark: #9c0a0e;
  }
  html, body {
    margin: 0;
    width: 1200px;
    height: 1000px;
    overflow: hidden;
    background: var(--page-bg);
  }
  .screen {
    position: absolute;
    left: 0; top: 100px;
    width: 1200px; height: 800px;
    background:
      repeating-linear-gradient(0deg, var(--screen-grid) 0 1px, transparent 1px 4px),
      repeating-linear-gradient(90deg, var(--screen-grid) 0 1px, transparent 1px 4px),
      radial-gradient(ellipse at 50% 30%, #8a2023, var(--screen-bg) 70%);
    font-family: "Noto Sans", sans-serif;
    font-weight: 700;
    color: var(--label);
  }
  .lcd {
    position: absolute;
    left: 155px; top: 42px;
    width: 890px; height: 222px;
    border-radius: 6px;
    background: linear-gradient(180deg, var(--lcd-top), var(--lcd-bottom));
    box-shadow: inset 0 0 0 2px var(--lcd-edge), 0 2px 6px rgba(0,0,0,.35);
  }
  .lcd-line {
    position: absolute;
    right: 77px; bottom: 27px;
    display: flex;
    align-items: baseline;
    gap: 36px;
    font-family: "Orbitron", sans-serif;
    font-weight: 400;
    line-height: 0.74;
    color: var(--digit);
    text-shadow: 0 2px 3px rgba(0,0,0,.35);
    transform: scaleY(1.45);
    transform-origin: bottom right;
    white-space: nowrap;
  }
  .lcd-readout { font-size: 150px; letter-spacing: 2px; }
  .lcd-unit { font-size: 74px; }
  .section-label {
    position: absolute;
    font-size: 27px;
    line-height: 1;
    text-shadow: 0 1px 2px rgba(0,0,0,.6);
  }
  .section-label.tones { left: 111px; top: 282px; }
  .section-label.modifier { left: 0; width: 1202px; top: 528px; text-align: center; }
  .tone-panel {
    position: absolute;
    left: 87px; top: 324px;
    width: 1030px; height: 198px;
    border-radius: 22px;
    background: var(--panel);
    box-shadow: inset 0 0 10px rgba(0,0,0,.25);
  }
  .tone-grid {
    position: absolute;
    left: 108px; top: 331px;
    display: grid;
    grid-template-columns: repeat(6, 156px);
    grid-auto-rows: 79px;
    column-gap: 12px;
    row-gap: 27px;
  }
  .key {
    border-radius: 6px;
    background: linear-gradient(180deg, var(--key-top), var(--key-bottom));
    box-shadow: inset 0 1px 0 rgba(255,255,255,.45), 0 2px 4px rgba(0,0,0,.4);
    display: flex; align-items: center; justify-content: center;
    font-family: "Orbitron", sans-serif;
    font-weight: 400;
    font-size: 50px;
    color: #fff;
    text-shadow: 0 0 2px rgba(0,0,0,.55);
  }
  .key.is-down {
    background: linear-gradient(180deg, var(--key-down-top), var(--key-down-bottom));
    box-shadow: inset 0 2px 5px rgba(0,0,0,.45);
    color: var(--key-down-text);
    text-shadow: 0 1px 0 rgba(255,255,255,.35);
  }
  .control-label {
    position: absolute;
    top: 646px;
    width: 240px;
    text-align: center;
    font-size: 20px;
    text-shadow: 0 1px 2px rgba(0,0,0,.6);
  }
  .wobble-switch {
    position: absolute;
    left: 66px; top: 682px;
    width: 184px; height: 64px;
    border-radius: 7px;
    background: #d9d6d6;
    box-shadow: inset 0 0 0 3px #6a6466, 0 2px 4px rgba(0,0,0,.4);
    display: flex;
    font-size: 22px;
    overflow: hidden;
  }
  .wobble-switch span {
    flex: 1;
    display: flex; align-items: center; justify-content: center;
  }
  .wobble-switch .on { color: #9d9a9b; background: linear-gradient(180deg, #e8e6e6, #cfcccc); margin: 6px 0 6px 6px; border-radius: 4px 0 0 4px; }
  .wobble-switch .off { color: var(--switch-off); background: var(--switch-face); margin: 6px 6px 6px 0; border-radius: 0 4px 4px 0; }
  .mode-key {
    position: absolute;
    top: 677px;
    width: 145px; height: 74px;
    font-family: "Noto Sans", sans-serif;
    font-weight: 700;
    font-size: 42px;
  }
  .stop-button {
    position: absolute;
    left: 972px; top: 623px;
    width: 152px; height: 152px;
    border-radius: 50%;
    background: radial-gradient(circle at 45% 30%, var(--stop-light), var(--stop-dark) 75%);
    box-shadow: 0 4px 10px rgba(0,0,0,.5), inset 0 -4px 8px rgba(0,0,0,.3);
    display: flex; align-items: center; justify-content: center;
    font-family: "Oswald", sans-serif;
    font-weight: 500;
    font-size: 60px;
    color: #fff;
    text-shadow: 0 2px 3px rgba(0,0,0,.5);
  }
</style>
</head>
<body>
  <main class="screen">
    <section class="lcd">
      <div class="lcd-line">
        <span class="lcd-readout">55.8</span>
        <span class="lcd-unit">HZ</span>
      </div>
    </section>

    <div class="section-label tones">Frequency Tones</div>
    <div class="tone-panel"></div>
    <div class="tone-grid">
      <div class="key">20</div>
      <div class="key">30</div>
      <div class="key">40</div>
      <div class="key">50</div>
      <div class="key is-down">60</div>
      <div class="key">70</div>
      <div class="key">80</div>
      <div class="key">90</div>
      <div class="key">100</div>
      <div class="key">150</div>
      <div class="key">250</div>
      <div class="key">300</div>
    </div>
    <div class="section-label modifier">Frequency Modifier</div>

    <div class="control-label" style="left:38px">+10 Hz Wobble</div>
    <div class="wobble-switch"><span class="on">ON</span><span class="off">OFF</span></div>

    <div class="control-label" style="left:336px">Freq.Sweep</div>
    <div class="key mode-key" style="left:383px">S</div>

    <div class="control-label" style="left:633px">Pink Noise</div>
    <div class="key mode-key" style="left:680px">P</div>

    <div class="stop-button">STOP</div>
  </main>
</body>
</html>
```